Welcome Postcard for existing church in new facility

I need a postcard to express the 4 strong points of our ministry. I have attached a sample postcard that we really liked as a start point. Our four strengths are;

LOVE
WORSHIP
DIVERSITY
DOCTRINE

I want to make sure the colors used are vivid and provide plenty of pop.

I have provide images to coincide with the four ministry strengths and they are named according the the strength the coincide with, pick whichever you think is best graphically.

our twitter handle is @BHDAWNOK
our FB handle is /BHDAWNOK
our Youtube handle is /BrightHarbor

I must have all PSD layers in case last minutes changes need to be made. THIS IS A REQUIREMENT.

Target Market(s)

General Population

Industry/Entity Type

Non-Profit

Font styles to use
Sans Serif

Requirements
Must have
• I must have all PSD layers in case last minutes changes need to be made. THIS IS A REQUIREMENT.
Nice to have
• Be attractive and market friendly is US marketplace
Should not have
• Please do not submit multiple designs with slight deviations. If you submit multiple designs please make them totally different one from another. We will not consider your design if you spam us.

```html
<!DOCTYPE html>
<html lang="en">
<head>
<meta charset="utf-8">
<title>Bright Harbor Welcome Postcard</title>
<link rel="stylesheet" href="https://fonts.googleapis.com/css2?family=Montserrat:wght@600&display=swap">
<style>
  :root {
    --doctrine-red: #e0261a;
    --doctrine-coral: #ee6a45;
    --doctrine-peach: #f0a07c;
    --doctrine-dark: #120c0a;
    --love-light: #f3eee8;
    --love-pink: #f2a58c;
    --love-skin: #ea8a6c;
    --love-mint: #74dcaa;
    --love-teal: #3fd49a;
    --worship-orange: #f6a311;
    --worship-gold: #f5c35e;
    --worship-amber: #e39a3c;
    --worship-green: #3f8a6c;
    --worship-dark: #262b28;
    --diversity-lime: #a4dc10;
    --diversity-yellow: #cde658;
    --diversity-light: #ece8dc;
    --diversity-grey: #8c9694;
    --diversity-denim: #4a5d72;
    --divider: #1e1e1e;
    --label: #ffffff;
  }
  html, body {
    margin: 0;
    padding: 0;
    width: 1200px;
    height: 783px;
    overflow: hidden;
    background: #ffffff;
  }
  .postcard {
    display: block;
    width: 1200px;
    height: 783px;
  }
  .strength-label {
    font-family: "Montserrat", sans-serif;
    font-weight: 600;
    font-size: 39px;
    fill: var(--label);
    letter-spacing: 0.5px;
  }
  .label-rule {
    fill: none;
    stroke: var(--label);
    stroke-width: 2.5;
  }
  .panel-divider {
    stroke: var(--divider);
    stroke-width: 3;
  }
</style>
</head>
<body>
<svg class="postcard" viewBox="0 0 1294 844" preserveAspectRatio="none" xmlns="http://www.w3.org/2000/svg">
  <defs>
    <linearGradient id="doctrineFill" x1="0" y1="0" x2="0" y2="1">
      <stop offset="0" stop-color="var(--doctrine-dark)"/>
      <stop offset="0.22" stop-color="#3a1a12"/>
      <stop offset="0.4" stop-color="var(--doctrine-peach)"/>
      <stop offset="0.62" stop-color="var(--doctrine-coral)"/>
      <stop offset="1" stop-color="var(--doctrine-red)"/>
    </linearGradient>
    <linearGradient id="loveFill" x1="0" y1="0" x2="0" y2="1">
      <stop offset="0" stop-color="var(--love-light)"/>
      <stop offset="0.28" stop-color="var(--love-pink)"/>
      <stop offset="0.5" stop-color="var(--love-skin)"/>
      <stop offset="0.72" stop-color="var(--love-mint)"/>
      <stop offset="1" stop-color="var(--love-teal)"/>
    </linearGradient>
    <linearGradient id="worshipFill" x1="0" y1="0" x2="0" y2="1">
      <stop offset="0" stop-color="var(--worship-orange)"/>
      <stop offset="0.28" stop-color="var(--worship-gold)"/>
      <stop offset="0.48" stop-color="var(--worship-amber)"/>
      <stop offset="0.75" stop-color="var(--worship-green)"/>
      <stop offset="1" stop-color="var(--worship-dark)"/>
    </linearGradient>
    <linearGradient id="diversityFill" x1="0" y1="0" x2="0" y2="1">
      <stop offset="0" stop-color="var(--diversity-lime)"/>
      <stop offset="0.28" stop-color="var(--diversity-yellow)"/>
      <stop offset="0.52" stop-color="var(--diversity-light)"/>
      <stop offset="0.78" stop-color="var(--diversity-grey)"/>
      <stop offset="1" stop-color="var(--diversity-denim)"/>
    </linearGradient>
  </defs>

  <!-- Strength panels -->
  <polygon class="panel panel-doctrine" fill="url(#doctrineFill)" points="0,0 10,0 495,844 0,844"
           role="img" aria-label="Photo of an open Bible with a red tint"/>
  <polygon class="panel panel-love" fill="url(#loveFill)" points="10,0 415,0 890,844 495,844"
           role="img" aria-label="Photo of two women sharing a joyful hug"/>
  <polygon class="panel panel-worship" fill="url(#worshipFill)" points="415,0 800,0 1294,844 890,844"
           role="img" aria-label="Photo of a keyboardist leading worship in the sanctuary"/>
  <polygon class="panel panel-diversity" fill="url(#diversityFill)" points="800,0 1294,0 1294,844"
           role="img" aria-label="Photo of a diverse congregation praying together"/>

  <line class="panel-divider" x1="10" y1="0" x2="495" y2="844"/>
  <line class="panel-divider" x1="415" y1="0" x2="890" y2="844"/>
  <line class="panel-divider" x1="800" y1="0" x2="1294" y2="844"/>

  <!-- Colour bands -->
  <polygon class="band band-doctrine" fill="var(--doctrine-red)" points="0,820 481,820 495,844 0,844"/>
  <polygon class="band band-love" fill="var(--love-teal)" points="495,820 877,820 890,844 495,844"/>
  <polygon class="band band-worship" fill="var(--worship-orange)" points="415,0 800,0 816,28 431,28"/>
  <polygon class="band band-diversity" fill="var(--diversity-lime)" points="800,0 1294,0 1294,28 816,28"/>

  <!-- Labels -->
  <g class="strength strength-doctrine">
    <text class="strength-label" x="48" y="613">DOCTRINE</text>
    <polyline class="label-rule" points="50,630 268,630 388,844"/>
  </g>
  <g class="strength strength-worship">
    <polyline class="label-rule" points="545,0 622,135 850,135"/>
    <text class="strength-label" x="640" y="195">WORSHIP</text>
  </g>
  <g class="strength strength-love">
    <text class="strength-label" x="571" y="743">LOVE</text>
    <polyline class="label-rule" points="572,758 680,758 730,844"/>
  </g>
  <g class="strength strength-diversity">
    <text class="strength-label" x="964" y="92">DIVERSITY</text>
    <polyline class="label-rule" points="970,108 1186,108 1294,300"/>
  </g>
</svg>
</body>
</html>
```